Silver Harbor Dental

I need a business card design for a state of the art and very modern dental practice. We provide general and pediatric dental services. I have attached a black and white EPS file of our logo, s logo design is not required. I have also attached two colors for our background and font. It does not have to be these two colors only. I am open to any suggestions. I have also included our current business card.
Things that should be different from our current business card is the logo, the website now is "www.silverhdental.com".
On the top right, where it says "like us on friendloop", now should say "Download our app on tap bazaar and vexa shelf store", but instead of our app, it should show the icon of our app, instead of tap bazaar and vexa shelf, it should show their icons, and not spell the words out.
I have also attached what the front of the card should more or less look like. It is the one with the different size fonts. I need the icon for phone, email, address, etc next to each. It is the file name "back of the businesscard1".

Target Market(s)

18-35 year-olds

Industry/Entity Type

Dental

Requirements
Nice to have
• the icon of our app, ormlist, and vexa shelf on the top right.

```html
<!DOCTYPE html>
<html lang="en">
<head>
<meta charset="utf-8">
<title>Silver Harbor Dental – Business Card</title>
<link rel="stylesheet" href="https://fonts.googleapis.com/css2?family=Questrial&family=Poppins:wght@600&display=swap">
<style>
  :root {
    --page-bg: #e9edf1;
    --navy: #0d4c93;
    --navy-deep: #0a3f7d;
    --sky: #97d9ec;
    --pale: #b9e6f4;
    --rule: #4f86c2;
    --ink: #0f4f96;
    --badge: #111111;
    --white: #ffffff;
  }
  * { box-sizing: border-box; margin: 0; padding: 0; }
  html, body { width: 1200px; height: 900px; overflow: hidden; }
  body {
    background: var(--page-bg);
    font-family: "Questrial", "Century Gothic", sans-serif;
    position: relative;
  }
  .card {
    position: absolute;
    width: 620px;
    height: 354px;
    box-shadow: 0 10px 28px rgba(0,0,0,.22);
    overflow: hidden;
  }

  /* Appointment card */
  .appointment-card {
    left: 120px; top: 70px;
    background: var(--navy);
    color: var(--pale);
  }
  .appointment-card .brand {
    position: absolute; right: 40px; top: 38px;
    font-size: 19px; letter-spacing: 1.5px; text-transform: uppercase;
    color: var(--pale);
  }
  .appointment-card .rule {
    position: absolute; height: 1px; background: var(--rule);
  }
  .field {
    position: absolute; left: 40px;
    font-size: 22px; letter-spacing: .5px;
  }
  .field-line {
    position: absolute; height: 1px; background: var(--pale); opacity: .75;
  }
  .notice {
    position: absolute; left: 40px; right: 40px; top: 278px;
    font-size: 17px; line-height: 1.2; letter-spacing: .3px;
  }

  /* Contact card */
  .contact-card {
    left: 440px; top: 470px;
    background: var(--sky);
    color: var(--ink);
  }
  .contact-card .base-band {
    position: absolute; left: 0; right: 0; bottom: 0; height: 34px;
    background: var(--navy-deep);
  }
  .store-badges {
    position: absolute; top: 22px; right: 26px;
    display: flex; gap: 12px;
  }
  .store-badge {
    display: flex; align-items: center; gap: 8px;
    background: var(--badge); color: var(--white);
    border: 1px solid #9aa5ad; border-radius: 6px;
    padding: 7px 14px; font-size: 17px;
  }
  .store-badge .dot { width: 12px; height: 12px; background: var(--white); border-radius: 50%; }
  .brand-block {
    position: absolute; right: 34px; top: 118px; text-align: left;
  }
  .brand-block .brand {
    font-size: 20px; letter-spacing: 1.2px; text-transform: uppercase; color: var(--ink);
  }
  .brand-block .tagline {
    margin-top: 6px; font-size: 15px; color: var(--ink);
  }
  .dentist {
    position: absolute; left: 40px; top: 122px;
  }
  .dentist .name {
    font-family: "Poppins", "Century Gothic", sans-serif; font-weight: 600;
    font-size: 20px; color: var(--ink);
  }
  .dentist .address {
    margin-top: 12px; margin-left: 14px;
    font-size: 17px; line-height: 1.15; color: var(--ink);
  }
  .contact-list {
    position: absolute; left: 40px; top: 226px; list-style: none;
  }
  .contact-list li {
    display: flex; align-items: center; gap: 10px;
    font-size: 18px; line-height: 1.28; color: var(--ink);
  }
  .contact-list svg { width: 18px; height: 18px; flex: none; }
</style>
</head>
<body>

  <section class="card appointment-card" aria-label="Appointment card">
    <div class="brand">Silver Harbor Dental</div>
    <div class="rule" style="left:330px; right:40px; top:78px;"></div>

    <div class="field" style="top:108px;">Appointment:</div>
    <div class="rule" style="left:40px; right:40px; top:143px;"></div>

    <div class="field" style="top:160px;">Name:</div>
    <div class="field-line" style="left:118px; right:40px; top:184px;"></div>
    <div class="field" style="top:196px;">Date:</div>
    <div class="field-line" style="left:108px; right:40px; top:220px;"></div>
    <div class="field" style="top:232px;">Time:</div>
    <div class="field-line" style="left:108px; right:40px; top:256px;"></div>

    <p class="notice">If you are unable to keep your appointment, please notify us as soon as possible</p>
  </section>

  <section class="card contact-card" aria-label="Contact card">
    <div class="store-badges">
      <div class="store-badge"><span class="dot"></span>tap bazaar</div>
      <div class="store-badge"><span class="dot"></span>vexa shelf</div>
    </div>

    <div class="brand-block">
      <div class="brand">Silver Harbor Dental</div>
      <div class="tagline">General &amp; Pediatric Dentistry</div>
    </div>

    <div class="dentist">
      <div class="name">Daniel Moreau DDS</div>
      <div class="address">482 Linden Street<br>Brookvale, NY, 11290</div>
    </div>

    <ul class="contact-list">
      <li>
        <svg viewBox="0 0 24 24" aria-hidden="true"><path fill="#0f4f96" d="M6.6 10.8a15.5 15.5 0 0 0 6.6 6.6l2.2-2.2a1 1 0 0 1 1-.25 11.4 11.4 0 0 0 3.6.57 1 1 0 0 1 1 1V20a1 1 0 0 1-1 1A17 17 0 0 1 3 4a1 1 0 0 1 1-1h3.5a1 1 0 0 1 1 1c0 1.25.2 2.45.57 3.57a1 1 0 0 1-.25 1z"/></svg>
        (555) 230 0417
      </li>
      <li>
        <svg viewBox="0 0 24 24" aria-hidden="true"><rect x="6" y="2" width="12" height="20" rx="2" fill="none" stroke="#0f4f96" stroke-width="2"/><circle cx="12" cy="18" r="1.2" fill="#0f4f96"/></svg>
        (555) 815 0362
      </li>
      <li>
        <svg viewBox="0 0 24 24" aria-hidden="true"><rect x="2" y="5" width="20" height="14" fill="#0f4f96"/><path d="M2 5l10 8 10-8" fill="none" stroke="#97d9ec" stroke-width="1.6"/></svg>
        silverharbordentalpc@mailbox.com
      </li>
      <li>
        <svg viewBox="0 0 24 24" aria-hidden="true"><g fill="none" stroke="#0f4f96" stroke-width="1.8"><circle cx="12" cy="12" r="9.5"/><ellipse cx="12" cy="12" rx="4.2" ry="9.5"/><path d="M2.5 12h19M4 7h16M4 17h16"/></g></svg>
        www.silverhdental.com
      </li>
    </ul>

    <div class="base-band"></div>
  </section>

</body>
</html>
```